skincare creams for tired moms

I need a package and a logo design for a skincare company based in California called Lumen Petal. I make day and night cream, under eye cream, and body lotion. The first product I plan to launch is an under eye cream. It does not have to be in these colors but I do teals, greens, black, and cobalt blue.

The package is going to either be in a box or a bag. Either way I go it will be like a gift box or bag. The design should make the person feel like they are getting something special and luxurious just for them.

I have small kids and it is really difficult to find a chunk of time to myself to update or review.

Target Market(s)

mainly first time moms. I am making an under eye cream that does not use retinol but is still powerful enough to get rid of bags and dark circles.

Industry/Entity Type

Cosmetics

Logo Text

The package and logo should incorporate the name Lumen Petal.

Font styles to use
Decorative
Script

Colors

Designer to choose colors to be used in the design.

Requirements
Nice to have
• maybe focus more on Petal instead of Lumen. Also incorporate plants or flowers
Should not have
• not a huge fan of pink

```html
<!DOCTYPE html>
<html lang="en">
<head>
<meta charset="utf-8">
<title>Lumen Petal – Under Eye Cream Box</title>
<link href="https://fonts.googleapis.com/css2?family=Playfair+Display:wght@700&family=Jost:wght@300;400;500&display=swap" rel="stylesheet">
<style>
  :root {
    --bg: #f7f7f7;
    --panel-front: #ececec;
    --panel-side: #dedede;
    --band: #ffffff;
    --band-side: #f3f3f3;
    --teal: #159e99;
    --navy: #1f237a;
    --ink: #222222;
    --floral-light: #f4f4f4;
    --floral-mid: #e2e2e2;
  }
  * { margin: 0; padding: 0; box-sizing: border-box; }
  html, body { width: 1200px; height: 1056px; overflow: hidden; background: var(--bg); }
  .dieline { position: relative; width: 1200px; height: 1056px; }

  .panel { position: absolute; top: 150px; height: 780px; overflow: hidden; }
  .panel-side { left: 110px; width: 320px; background: var(--panel-side); }
  .panel-front { left: 430px; width: 660px; background: var(--panel-front); }

  .floral { position: absolute; left: 0; right: 0;
    background: radial-gradient(circle at 30% 40%, var(--floral-light), var(--floral-mid) 70%); }
  .floral-top { top: 0; height: 215px; }
  .floral-bottom { bottom: 0; height: 255px; }
  .panel-side .floral { background: radial-gradient(circle at 40% 50%, #ebebeb, #d6d6d6 75%); }

  .band { position: absolute; left: 0; right: 0; top: 215px; height: 310px; background: var(--band); }
  .panel-side .band { background: var(--band-side); }

  /* front label */
  .brand-dot { position: absolute; left: 50%; top: 18px; width: 40px; height: 40px; margin-left: -20px;
    border-radius: 50%; background: var(--teal); }
  .brand-name { position: absolute; left: 0; right: 0; top: 70px; text-align: center;
    font-family: "Playfair Display", serif; font-weight: 700; color: var(--teal); line-height: 1; }
  .brand-name .line-1 { display: block; font-size: 66px; letter-spacing: 1px; }
  .brand-name .line-2 { display: block; font-size: 92px; letter-spacing: 2px; margin-top: 4px; }
  .product { position: absolute; left: 120px; right: 120px; top: 238px; height: 58px;
    border-top: 2px solid var(--teal); border-bottom: 2px solid var(--teal);
    font-family: "Jost", sans-serif; font-weight: 400; font-size: 34px; color: var(--navy);
    text-align: center; line-height: 54px; letter-spacing: 0.5px; }
  .volume { position: absolute; left: 50%; bottom: 112px; transform: translateX(-50%);
    padding: 4px 18px; border: 2px solid var(--teal); border-radius: 22px; background: rgba(255,255,255,0.6);
    font-family: "Jost", sans-serif; font-weight: 300; font-size: 24px; color: var(--ink); white-space: nowrap; }

  /* side label */
  .ingredients { position: absolute; left: 26px; right: 26px; top: 22px; font-family: "Jost", sans-serif; }
  .ingredients h2 { font-weight: 400; font-size: 15px; color: var(--navy); text-align: center; letter-spacing: 0.5px;
    padding-bottom: 6px; border-bottom: 1.5px solid var(--teal); width: 110px; margin: 0 auto 16px; }
  .ingredients p { font-weight: 300; font-size: 11.5px; line-height: 1.55; color: var(--ink); text-align: justify; }
  .ingredients .claim { margin-top: 14px; font-weight: 500; font-size: 10.5px; color: var(--teal); text-align: center; }
</style>
</head>
<body>
<main class="dieline">
  <section class="panel panel-side" aria-label="Side panel">
    <div class="floral floral-top" role="img" aria-label="Soft grey floral pattern of flowers and vines"></div>
    <div class="band">
      <div class="ingredients">
        <h2>INGREDIENTS</h2>
        <p>Aqua, aloe leaf juice, squalane, caffeine, niacinamide, peptide complex, cucumber extract, chamomile flower water, green tea leaf extract, hyaluronic acid, shea butter, jojoba seed oil, vitamin E, glycerin, rosehip oil, calendula extract, cica extract, bakuchiol, plant cellulose, citric acid and a gentle natural preservative blend for daily care.</p>
        <p class="claim">100% ORGANIC, NATURAL AND CRUELTY FREE</p>
      </div>
    </div>
    <div class="floral floral-bottom" role="img" aria-label="Soft grey floral pattern of flowers and vines"></div>
  </section>

  <section class="panel panel-front" aria-label="Front panel">
    <div class="floral floral-top" role="img" aria-label="Soft grey floral pattern of flowers and vines"></div>
    <div class="band">
      <span class="brand-dot" aria-hidden="true"></span>
      <h1 class="brand-name"><span class="line-1">LUMEN</span><span class="line-2">PETAL</span></h1>
      <p class="product">UNDER EYE CREAM</p>
    </div>
    <div class="floral floral-bottom" role="img" aria-label="Soft grey floral pattern of flowers and vines"></div>
    <p class="volume">12ml | 0.41fl /oz</p>
  </section>
</main>
</body>
</html>
```